Business Card + Letterhead Design for BELMARSH IMPORTS INC.

We already have a logo; now we need a business card + letterhead. We import and distribute flags and souvenirs with an emphasis on soccer related memorabilia. We target various ethnic markets and sporting goods stores. "Wandering Keepsakes"

```html
<!DOCTYPE html>
<html lang="en">
<head>
<meta charset="utf-8">
<title>Belmarsh Imports Inc. — Business Card</title>
<link href="https://fonts.googleapis.com/css2?family=Roboto+Slab:wght@400;700&display=swap" rel="stylesheet">
<style>
  :root {
    --page: #e9e9e9;
    --card: #1c1b1c;
    --card-deep: #141314;
    --band: #8e1a1d;
    --accent: #c4262b;
    --text: #f2f2f2;
    --muted: #b9b9b9;
    --rule: #5a5a5a;
  }
  * { margin: 0; padding: 0; box-sizing: border-box; }
  html, body { width: 1200px; height: 991px; overflow: hidden; }
  body {
    background: var(--page);
    font-family: "Roboto Slab", Georgia, serif;
    position: relative;
  }
  .card {
    position: absolute;
    top: 341px;
    width: 540px;
    height: 309px;
    background: var(--card);
    overflow: hidden;
    box-shadow: 0 10px 24px rgba(0,0,0,.18);
  }
  .card--front { left: 40px; }
  .card--back  { left: 620px; }

  /* front */
  .brand {
    position: absolute; left: 28px; top: 28px;
    display: flex; align-items: center; gap: 12px;
  }
  .brand__dot {
    width: 30px; height: 30px; border-radius: 50%;
    background: var(--accent);
  }
  .brand__name {
    color: var(--text); font-weight: 700; font-size: 22px;
    letter-spacing: 2px; line-height: 1;
  }
  .faint-circle {
    position: absolute; left: 250px; top: 170px;
    width: 170px; height: 170px; border-radius: 50%;
    background: #262526;
  }
  .holder {
    position: absolute; right: 30px; top: 92px;
    display: flex; align-items: center; gap: 8px;
    color: var(--text); font-weight: 700; font-size: 16px; letter-spacing: .5px;
  }
  .holder__mark { width: 10px; height: 10px; background: var(--accent); }
  .contact {
    position: absolute; right: 48px; top: 134px;
    list-style: none; color: var(--muted); font-size: 11px; line-height: 18px;
  }
  .contact__company { color: var(--text); letter-spacing: .5px; margin-bottom: 2px; }
  .contact__row { display: flex; align-items: center; gap: 7px; }
  .contact__row svg { width: 10px; height: 10px; flex: none; }
  .contact__web { color: var(--text); font-weight: 700; margin-top: 2px; }
  .tagline {
    position: absolute; left: 0; right: 0; bottom: 0; height: 38px;
    background: var(--band);
    display: flex; align-items: center; justify-content: flex-end;
    padding-right: 22px;
    color: var(--text); font-size: 17px; letter-spacing: .3px;
  }

  /* back */
  .pattern-field {
    position: absolute; inset: 0;
    background: radial-gradient(circle at 50% 45%, #232223, var(--card-deep));
  }
  .back-plate {
    position: absolute; left: 0; right: 0; top: 104px; height: 96px;
    background: rgba(50,50,50,.55);
    display: flex; flex-direction: column; align-items: center; justify-content: center; gap: 8px;
  }
  .back-plate .brand { position: static; }
  .back-plate__web { color: var(--muted); font-size: 11px; letter-spacing: 2px; }
</style>
</head>
<body>

<section class="card card--front" aria-label="Business card front">
  <div class="faint-circle" aria-hidden="true"></div>
  <div class="brand">
    <span class="brand__dot" aria-hidden="true"></span>
    <span class="brand__name">BELMARSH IMPORTS</span>
  </div>

  <div class="holder">
    <span>DORIAN VELLACOTT</span>
    <span class="holder__mark" aria-hidden="true"></span>
  </div>

  <ul class="contact">
    <li class="contact__company">BELMARSH IMPORTS INC.</li>
    <li class="contact__row">
      <svg viewBox="0 0 10 10"><circle cx="5" cy="5" r="5" fill="#c4262b"/><path d="M3.2 2.6l1 1-.6.7a4 4 0 0 0 2 2l.7-.6 1 1-.8.8C4.6 7.3 2.7 5.4 2.4 3.4z" fill="#fff"/></svg>
      <span>(555) 310-2297</span>
    </li>
    <li class="contact__row">
      <svg viewBox="0 0 10 10"><circle cx="5" cy="5" r="5" fill="#c4262b"/><rect x="2.8" y="3" width="4.4" height="4" fill="#fff"/></svg>
      <span>(555) 482-7710</span>
    </li>
    <li class="contact__row">
      <svg viewBox="0 0 10 10"><circle cx="5" cy="5" r="5" fill="#c4262b"/><path d="M2.5 3.3h5v3.4h-5z M2.5 3.3l2.5 2 2.5-2" fill="none" stroke="#fff" stroke-width=".8"/></svg>
      <span>sales@belmarshimports.ca</span>
    </li>
    <li class="contact__web">www.belmarshimports.ca</li>
  </ul>

  <div class="tagline">Wandering Keepsakes</div>
</section>

<section class="card card--back" aria-label="Business card back">
  <div class="pattern-field" role="img" aria-label="Repeating small brand-mark pattern in dark grey on black"></div>
  <div class="back-plate">
    <div class="brand">
      <span class="brand__dot" aria-hidden="true"></span>
      <span class="brand__name">BELMARSH IMPORTS</span>
    </div>
    <span class="back-plate__web">www.belmarshimports.ca</span>
  </div>
</section>

</body>
</html>
```